Business cards and stationary
Law Offices of Delphine R. Okonkwo
Professional
Delphine R. Okonkwo, Esq.
417 N. Cedar Brook Lane
Suite C-320
Plantation, Florida 33991
Delphine@Glenmorelegalcounsel.example
www.Glenmorelegalcounsel.example
The card should match my current website and logo. The back of the card should state: Practice Areas
Estate Planning
Probate and Trust Administration
Tax Law and Structuring
Business Structuring
Please no scales of justice or gavels

```html
<!DOCTYPE html>
<html lang="en">
<head>
<meta charset="utf-8">
<title>Law Offices of Delphine R. Okonkwo — Business Card</title>
<link rel="stylesheet" href="https://fonts.googleapis.com/css2?family=Cinzel:wght@400;600&family=Lato:wght@400;700&display=swap">
<style>
  :root {
    --page: #e6e8ec;
    --blue: #2f5fc8;
    --blue-deep: #1d3f9e;
    --blue-light: #4a7ad8;
    --navy: #16275a;
    --white: #ffffff;
    --grey: #9aa0a8;
    --ink: #1b1e24;
    --text-on-blue: #e8eefc;
  }
  * { box-sizing: border-box; margin: 0; padding: 0; }
  html, body { width: 1200px; height: 991px; overflow: hidden; }
  body {
    background: var(--page);
    display: flex;
    align-items: center;
    justify-content: center;
    gap: 40px;
    font-family: "Lato", sans-serif;
  }
  .card {
    position: relative;
    width: 540px;
    height: 309px;
    border-radius: 22px;
    overflow: hidden;
    box-shadow: 0 10px 26px rgba(20, 30, 60, 0.22);
  }
  .card__art { position: absolute; inset: 0; width: 100%; height: 100%; }

  /* Front */
  .brand {
    position: absolute;
    top: 72px;
    left: 268px;
    display: flex;
    flex-direction: column;
    align-items: flex-start;
  }
  .brand__mark {
    display: flex;
    align-items: center;
    gap: 8px;
    font-family: "Cinzel", serif;
    font-weight: 600;
    font-size: 26px;
    color: var(--blue-deep);
    letter-spacing: 1px;
  }
  .brand__square { width: 14px; height: 14px; background: var(--navy); }
  .brand__office {
    margin-top: 6px;
    font-family: "Cinzel", serif;
    font-size: 11px;
    color: var(--ink);
    letter-spacing: 1.5px;
  }
  .brand__name {
    margin-top: 2px;
    padding-top: 3px;
    border-top: 1px solid var(--ink);
    font-family: "Cinzel", serif;
    font-size: 15px;
    color: var(--blue-deep);
    letter-spacing: 1.5px;
  }
  .contact {
    position: absolute;
    left: 22px;
    bottom: 22px;
    list-style: none;
    font-family: "Cinzel", serif;
    font-size: 9px;
    line-height: 1.65;
    color: var(--text-on-blue);
    letter-spacing: 0.6px;
  }
  .contact__item { display: flex; align-items: center; gap: 7px; }
  .contact__icon { width: 10px; height: 10px; flex: none; }
  .signature {
    position: absolute;
    right: 22px;
    bottom: 22px;
    text-align: right;
    font-family: "Cinzel", serif;
    color: var(--text-on-blue);
    letter-spacing: 0.8px;
  }
  .signature__name { font-size: 10px; }
  .signature__title { font-size: 8px; opacity: 0.85; margin-top: 2px; }

  /* Back */
  .card--back {
    background: linear-gradient(160deg, var(--blue-light) 0%, var(--blue) 45%, var(--blue-deep) 100%);
    display: flex;
    flex-direction: column;
    align-items: center;
    padding-top: 40px;
    color: var(--text-on-blue);
    font-family: "Cinzel", serif;
  }
  .back__brand {
    display: flex;
    align-items: center;
    gap: 10px;
    font-weight: 600;
    font-size: 36px;
    line-height: 1;
    color: var(--white);
    letter-spacing: 2px;
  }
  .back__square { width: 18px; height: 18px; background: var(--navy); }
  .back__url {
    margin-top: 14px;
    font-size: 10px;
    letter-spacing: 3px;
  }
  .practice {
    margin-top: 18px;
    padding-top: 12px;
    width: 300px;
    border-top: 1px solid rgba(232, 238, 252, 0.45);
    text-align: center;
  }
  .practice__title {
    font-size: 12px;
    font-weight: 600;
    color: var(--white);
    letter-spacing: 2px;
    margin-bottom: 6px;
  }
  .practice__list {
    list-style: none;
    font-size: 10px;
    line-height: 1.7;
    letter-spacing: 1px;
  }
</style>
</head>
<body>

  <section class="card card--front" aria-label="Business card front">
    <svg class="card__art" viewBox="0 0 540 309" preserveAspectRatio="none" aria-hidden="true">
      <defs>
        <linearGradient id="frontBlue" x1="0" y1="0" x2="1" y2="1">
          <stop offset="0" stop-color="#4a7ad8"/>
          <stop offset="0.5" stop-color="#2f5fc8"/>
          <stop offset="1" stop-color="#1d3f9e"/>
        </linearGradient>
        <linearGradient id="frontPaper" x1="0" y1="0" x2="0" y2="1">
          <stop offset="0" stop-color="#ffffff"/>
          <stop offset="1" stop-color="#e9ebee"/>
        </linearGradient>
      </defs>
      <rect width="540" height="309" fill="url(#frontBlue)"/>
      <path d="M150 0 H540 V250 C420 205 300 190 210 200 C170 130 150 60 150 0 Z" fill="#9aa0a8"/>
      <path d="M162 0 H540 V240 C420 196 300 182 218 190 C182 124 164 58 162 0 Z" fill="#1b1e24"/>
      <path d="M168 0 H540 V234 C420 190 300 176 222 184 C188 120 170 56 168 0 Z" fill="url(#frontPaper)"/>
    </svg>

    <div class="brand">
      <div class="brand__mark"><span class="brand__square"></span>Okonkwo</div>
      <p class="brand__office">Law Offices of</p>
      <p class="brand__name">Delphine R. Okonkwo</p>
    </div>

    <ul class="contact">
      <li class="contact__item">
        <svg class="contact__icon" viewBox="0 0 10 10"><path d="M5 0.5a3 3 0 0 1 3 3c0 2.2-3 6-3 6s-3-3.8-3-6a3 3 0 0 1 3-3z" fill="#e8eefc"/><circle cx="5" cy="3.5" r="1" fill="#2f5fc8"/></svg>
        417 N. Cedar Brook Lane
      </li>
      <li class="contact__item"><span class="contact__icon"></span>Suite C-320</li>
      <li class="contact__item"><span class="contact__icon"></span>Plantation, Florida 33991</li>
      <li class="contact__item">
        <svg class="contact__icon" viewBox="0 0 10 10"><path d="M2 0.8l2 2-1 1.2a6 6 0 0 0 3 3l1.2-1 2 2-1.2 1.5C4.5 9.5 0.5 5.5 0.5 2z" fill="#e8eefc"/></svg>
        Tel (954) 555-0182
      </li>
      <li class="contact__item">
        <svg class="contact__icon" viewBox="0 0 10 10"><rect x="0.5" y="2" width="9" height="6" fill="none" stroke="#e8eefc"/><path d="M0.5 2l4.5 3.5 4.5-3.5" fill="none" stroke="#e8eefc"/></svg>
        Delphine@Glenmorelegalcounsel.example
      </li>
      <li class="contact__item">
        <svg class="contact__icon" viewBox="0 0 10 10"><circle cx="5" cy="5" r="4.3" fill="none" stroke="#e8eefc"/><path d="M0.7 5h8.6M5 0.7c-2 2.5-2 6 0 8.6M5 0.7c2 2.5 2 6 0 8.6" fill="none" stroke="#e8eefc" stroke-width="0.7"/></svg>
        www.Glenmorelegalcounsel.example
      </li>
    </ul>

    <div class="signature">
      <p class="signature__name">Delphine R. Okonkwo, Esq.</p>
      <p class="signature__title">Attorney at Law</p>
    </div>
  </section>

  <section class="card card--back" aria-label="Business card back">
    <div class="back__brand"><span class="back__square"></span>Okonkwo</div>
    <p class="back__url">www.Glenmorelegalcounsel.example</p>
    <div class="practice">
      <h2 class="practice__title">Practice Areas</h2>
      <ul class="practice__list">
        <li>Estate Planning</li>
        <li>Probate and Trust Administration</li>
        <li>Tax Law and Structuring</li>
        <li>Business Structuring</li>
      </ul>
    </div>
  </section>

</body>
</html>
```